Business card for auto dealership

Looking for a clean modern design.
Would like attached logo incorporated

Industry/Entity Type

Car dealership

Contact Information for Business Card

Name, website, phone, cell, fax, email

```html
<!DOCTYPE html>
<html lang="en">
<head>
<meta charset="utf-8">
<title>Hollins Truck &amp; Auto Sales — Business Card</title>
<link href="https://fonts.googleapis.com/css2?family=Montserrat:wght@400;600;700&display=swap" rel="stylesheet">
<style>
  :root {
    --backdrop: #d6d6d6;
    --card: #efefed;
    --ink: #111111;
    --muted: #7a7a7a;
    --rule: #d9d9d6;
  }
  html, body {
    margin: 0;
    width: 1200px;
    height: 1051px;
    overflow: hidden;
    background: var(--backdrop);
    font-family: "Montserrat", sans-serif;
  }
  .canvas {
    position: relative;
    width: 1200px;
    height: 1051px;
  }
  .card {
    position: absolute;
    top: 377px;
    width: 520px;
    height: 297px;
    background: var(--card);
    box-shadow: 0 2px 6px rgba(0,0,0,0.12);
    box-sizing: border-box;
  }
  .card--front { left: 50px; }
  .card--back { left: 630px; display: flex; align-items: center; justify-content: center; }

  .brand {
    color: var(--ink);
    font-weight: 700;
    line-height: 1.1;
  }
  .brand__name { display: block; }
  .brand__tag { display: block; letter-spacing: 0.08em; }

  .card--front .brand {
    position: absolute;
    left: 34px;
    top: 96px;
    width: 200px;
  }
  .card--front .brand__name { font-size: 40px; }
  .card--front .brand__tag { font-size: 11px; margin-top: 4px; }

  .card--back .brand { text-align: center; }
  .card--back .brand__name { font-size: 72px; }
  .card--back .brand__tag { font-size: 17px; margin-top: 6px; }

  .divider {
    position: absolute;
    left: 262px;
    top: 70px;
    width: 1px;
    height: 160px;
    background: var(--rule);
  }
  .contact {
    position: absolute;
    left: 282px;
    top: 72px;
  }
  .contact__name {
    margin: 0 0 12px;
    font-size: 17px;
    font-weight: 700;
    color: var(--ink);
  }
  .contact__list {
    list-style: none;
    margin: 0;
    padding: 0;
  }
  .contact__item {
    display: flex;
    align-items: center;
    gap: 8px;
    font-size: 13px;
    font-weight: 400;
    color: var(--muted);
    line-height: 21px;
  }
  .contact__icon {
    width: 11px;
    height: 11px;
    fill: var(--ink);
    flex: none;
  }
</style>
</head>
<body>
<main class="canvas">
  <section class="card card--front" aria-label="Business card front">
    <div class="brand">
      <span class="brand__name">Hollins</span>
      <span class="brand__tag">TRUCK &amp; AUTO SALES</span>
    </div>
    <div class="divider"></div>
    <div class="contact">
      <h1 class="contact__name">Dana Whitfield</h1>
      <ul class="contact__list">
        <li class="contact__item">
          <svg class="contact__icon" viewBox="0 0 12 12" aria-hidden="true"><path d="M2.5 1 4.5 3.2 3.4 4.6C4 6 5.6 7.7 7.4 8.6L8.8 7.5 11 9.5 9.8 11C5.2 10.6 1.4 6.8 1 2.2Z"/></svg>
          555-201-4830
        </li>
        <li class="contact__item">
          <svg class="contact__icon" viewBox="0 0 12 12" aria-hidden="true"><path d="M3 0h6v12H3ZM4 1.5v8h4v-8Z"/></svg>
          555-317-6092
        </li>
        <li class="contact__item">
          <svg class="contact__icon" viewBox="0 0 12 12" aria-hidden="true"><path d="M3 0h6v3H3ZM1 4h10v5H9v3H3V9H1ZM4 7.5v3h4v-3Z"/></svg>
          555-442-9158
        </li>
        <li class="contact__item">
          <svg class="contact__icon" viewBox="0 0 12 12" aria-hidden="true"><path d="M0 2h12v1L6 7 0 3ZM0 4.5l6 4 6-4V10H0Z"/></svg>
          dana@hollinsauto.com
        </li>
        <li class="contact__item">
          <svg class="contact__icon" viewBox="0 0 12 12" aria-hidden="true"><circle cx="6" cy="6" r="6"/></svg>
          Hollinsauto.com
        </li>
      </ul>
    </div>
  </section>

  <section class="card card--back" aria-label="Business card back">
    <div class="brand">
      <span class="brand__name">Hollins</span>
      <span class="brand__tag">TRUCK &amp; AUTO SALES</span>
    </div>
  </section>
</main>
</body>
</html>
```